LUSTRIA INC. is a new Fashion Stylist, Design Merchandiser, and consultant in the fashion industry

We need a logo design for a new Calgary, Alberta based company that is in the business of making over your image, wardrobe and style for both business and personal purposes.

Target Market(s)

Professional female and male business people looking for a new style or complete fashion makeover including clothes closet merchandising and makeover.

Contact Information for Business Card

Number of Pages Required

1 page

Font styles to use
Script

Colors
fac994
fbe7d2
fee3d4

Requirements
Must have
• Fashion Industry theme that is very elegant and colorful using gold/bronze/silver color themes.
Nice to have
• Incorporate the company name with the creative font to come up with the appropriate "logo"

```html
<!DOCTYPE html>
<html lang="en">
<head>
<meta charset="utf-8">
<title>Lustria Inc. – Business Card</title>
<link rel="stylesheet" href="https://fonts.googleapis.com/css2?family=Oswald:wght@600&family=Poppins:wght@300;400&display=swap">
<style>
  :root {
    --page-bg: #ffffff;
    --card-dark: #1f1f1f;
    --card-light: #f7f7f7;
    --gold: #d9a520;
    --ink: #3f3f3f;
    --card-shadow: rgba(0, 0, 0, 0.18);
  }
  * { margin: 0; padding: 0; box-sizing: border-box; }
  html, body {
    width: 1200px;
    height: 1000px;
    overflow: hidden;
    background: var(--page-bg);
  }
  .canvas {
    position: relative;
    width: 1200px;
    height: 1000px;
  }
  .card {
    position: absolute;
    top: 101px;
    width: 456px;
    height: 797px;
    box-shadow: 0 2px 10px var(--card-shadow);
  }
  .card--front {
    left: 120px;
    background: var(--card-dark);
  }
  .card--back {
    left: 625px;
    background: var(--card-light);
    font-family: "Poppins", sans-serif;
    color: var(--ink);
  }
  .wordmark-vertical {
    position: absolute;
    inset: 0;
    width: 456px;
    height: 797px;
  }
  .wordmark-vertical text {
    font-family: "Oswald", sans-serif;
    font-weight: 600;
    font-size: 122px;
  }
  .back-content {
    position: absolute;
    left: 30px;
    top: 553px;
  }
  .company-name {
    font-weight: 400;
    font-size: 30px;
    letter-spacing: 1.5px;
    color: var(--gold);
    line-height: 1;
  }
  .person-name {
    margin-top: 40px;
    font-weight: 400;
    font-size: 23px;
    line-height: 1.1;
  }
  .person-role {
    font-weight: 300;
    font-size: 17px;
    line-height: 1.2;
  }
  .contact-list {
    margin-top: 24px;
    list-style: none;
    font-weight: 300;
    font-size: 18px;
    line-height: 23px;
  }
</style>
</head>
<body>
  <main class="canvas">
    <section class="card card--front" aria-label="Card front">
      <svg class="wordmark-vertical" viewBox="0 0 456 797" xmlns="http://www.w3.org/2000/svg">
        <defs>
          <linearGradient id="gold-foil" x1="0" y1="0" x2="1" y2="1">
            <stop offset="0" stop-color="#b8820f"/>
            <stop offset="0.3" stop-color="#f2cf5e"/>
            <stop offset="0.55" stop-color="#c9951c"/>
            <stop offset="0.8" stop-color="#f5d772"/>
            <stop offset="1" stop-color="#a87510"/>
          </linearGradient>
        </defs>
        <text transform="translate(428 777) rotate(-90)" x="0" y="0"
              textLength="752" lengthAdjust="spacing"
              fill="url(#gold-foil)">LUSTRIA INC.</text>
      </svg>
    </section>

    <section class="card card--back" aria-label="Card back">
      <div class="back-content">
        <p class="company-name">LUSTRIA INC.</p>
        <p class="person-name">Maren Holloway</p>
        <p class="person-role">fashion stylist</p>
        <ul class="contact-list">
          <li>Tel: 403-555-0148</li>
          <li>Mail: hello@lustriastudio.com</li>
          <li>Web: lustriastudio.com</li>
        </ul>
      </div>
    </section>
  </main>
</body>
</html>
```